Create a responsive HTML email template

We need a basic HTML email template for corporate communications. Template should feature header with our logo and email title. Below that should be the email body - text only. Below that should be the footer with an unsubscribe link, phone, website, contact us link and bit of small print text for disclaimers.

Our colours and branding can be found here: [login to view URL]

```html
<!DOCTYPE html>
<html lang="en">
<head>
<meta charset="utf-8">
<title>Hearthwise Newsletter</title>
<link rel="stylesheet" href="https://fonts.googleapis.com/css2?family=Roboto+Slab:wght@300;400;700&family=Roboto:wght@400;500&display=swap">
<style>
  :root {
    --brand: #0aa1dc;
    --brand-light: #5cc6ee;
    --brand-text: #1b9fd6;
    --ink: #3c3c3c;
    --dark: #4a484f;
    --white: #ffffff;
    --field-line: #9bb8c6;
  }
  * { box-sizing: border-box; margin: 0; padding: 0; }
  html, body { width: 1200px; height: 643px; overflow: hidden; background: var(--white); }
  body { position: relative; font-family: "Roboto Slab", Georgia, serif; color: var(--ink); }

  .site-header {
    position: absolute; left: 0; top: 0; width: 1200px; height: 70px;
    background: var(--white); box-shadow: 0 2px 4px rgba(0,0,0,0.18);
  }
  .brand { position: absolute; left: 76px; top: 15px; display: flex; align-items: center; gap: 10px; }
  .brand-mark { width: 30px; height: 30px; border-radius: 50%; background: var(--brand-text); }
  .brand-name { font-size: 30px; font-weight: 400; color: var(--brand-text); line-height: 40px; }
  .header-email {
    position: absolute; left: 863px; top: 19px; display: flex; align-items: center; gap: 8px;
    font-size: 21px; font-weight: 700; color: var(--brand-text); line-height: 28px;
  }

  .title-band {
    position: absolute; left: 60px; top: 73px; width: 1080px; height: 37px;
    background: linear-gradient(to bottom, var(--brand-light), var(--brand) 45%);
    text-align: center; line-height: 37px;
    font-size: 20px; font-style: italic; color: #333;
  }

  .letter { position: absolute; left: 76px; top: 133px; width: 1030px; }
  .greeting { font-size: 22px; line-height: 28px; font-weight: 700; font-style: italic; color: var(--brand-text); margin-bottom: 20px; }
  .letter p { font-size: 13px; font-weight: 300; line-height: 16px; color: var(--ink); margin-bottom: 14px; }
  .regards { font-size: 13px; line-height: 16px; font-weight: 700; font-style: italic; color: var(--brand-text); }
  .signature { font-size: 21px; line-height: 26px; font-weight: 700; font-style: italic; color: var(--brand-text); margin-top: 12px; }

  .footer-panel {
    position: absolute; left: 60px; top: 391px; width: 1080px; height: 200px; background: var(--brand);
  }
  .contact-form { position: absolute; left: 21px; top: 20px; width: 360px; }
  .field {
    display: block; width: 359px; height: 22px; border: 1px solid var(--field-line); background: var(--white);
    font-family: Roboto, Arial, sans-serif; font-size: 11px; color: #555; padding: 3px; margin-bottom: 10px;
  }
  .field-message { height: 60px; font-family: "Roboto Mono", monospace; font-size: 10px; resize: none; }
  .submit {
    display: block; width: 360px; height: 26px; background: var(--dark); border: none;
    font-family: Roboto, Arial, sans-serif; font-size: 16px; color: var(--brand-light); text-align: center; line-height: 26px;
  }

  .contact { position: absolute; left: 453px; top: 16px; width: 400px; }
  .contact-title { font-size: 21px; font-weight: 400; color: #333; line-height: 26px; }
  .contact-rule { width: 160px; height: 4px; border-top: 2px solid #e8f6fc; border-bottom: 1px solid #4a6f80; margin: 1px 0 10px; }
  .contact-row { display: flex; align-items: center; gap: 18px; height: 23px; font-size: 12px; color: #222; }
  .contact-address { font-size: 12px; color: #3f5a66; margin-top: 3px; font-weight: 300; }
  .social { display: flex; gap: 17px; margin-top: 7px; }
  .social-item { width: 32px; height: 32px; }
  .social-a { background: #3b5b95; }
  .social-b { background: #d24a3c; }
  .social-c { background: #c5a46a; }

  .copyright {
    position: absolute; left: 60px; top: 591px; width: 1080px; height: 49px; background: var(--dark);
    color: var(--white); text-align: center; line-height: 49px; font-size: 13px; font-weight: 700;
  }
</style>
</head>
<body>
  <header class="site-header">
    <div class="brand">
      <span class="brand-mark"></span>
      <span class="brand-name">Hearthwise</span>
    </div>
    <div class="header-email">
      <svg width="30" height="24" viewBox="0 0 30 24" aria-hidden="true">
        <rect x="1" y="1" width="28" height="22" rx="2" fill="#1b9fd6"/>
        <path d="M2 3 L15 13 L28 3" stroke="#fff" stroke-width="2.5" fill="none"/>
      </svg>
      <span>hello@hearthwise.net</span>
    </div>
  </header>

  <div class="title-band">Lorem ipsum dolor sit amet</div>

  <main class="letter">
    <h1 class="greeting">Dear Hearthwise,</h1>
    <p>Lorem ipsum dolor sit, amet consectetur adipisicing elit. Aspernatur laborum amet error quae perspiciatis enim aut, vitae, et iste culpa alias voluptatum, hic quisquam rem totam quam obcaecati impedit sequi.</p>
    <p>Lorem ipsum, dolor sit amet consectetur adipisicing elit. Suscipit obcaecati quasi culpa, ad sit magni natus aut sint animi quaerat aliquid. Consequatur omnis blanditiis enim eaque delectus dolore natus reprehenderit dolorum quidem facilis vel quia quos, explicabo similique architecto non laudantium assumenda doloribus eligendi soluta? Quaerat consequuntur explicabo beatae itaque?</p>
    <p>Lorem ipsum dolor sit amet, consectetur adipisicing elit. Et, nulla dolorem quasi aperiam dolor sint optio laudantium asperiores nobis provident!</p>
    <div class="regards">Regards,</div>
    <div class="signature">Hearthwise Team</div>
  </main>

  <footer>
    <section class="footer-panel">
      <form class="contact-form">
        <input class="field" type="text" placeholder="Enter Your Name">
        <input class="field" type="email" placeholder="Enter Your Email">
        <textarea class="field field-message" placeholder="Enter text here..."></textarea>
        <button class="submit" type="button">Submit</button>
      </form>

      <div class="contact">
        <h2 class="contact-title">Contact Us</h2>
        <div class="contact-rule"></div>
        <div class="contact-row">
          <svg width="14" height="14" viewBox="0 0 14 14" aria-hidden="true">
            <rect width="14" height="14" rx="2" fill="#333"/>
            <path d="M4 3 L6 3 L6.6 5 L5.5 6 Q6.5 8 8 8.5 L9 7.4 L11 8 L11 10 Q9 11.5 6 9 Q3 6 4 3 Z" fill="#0aa1dc"/>
          </svg>
          <span>014-555-0192</span>
        </div>
        <div class="contact-row">
          <svg width="14" height="12" viewBox="0 0 14 12" aria-hidden="true">
            <rect width="14" height="12" rx="1" fill="#333"/>
            <path d="M1 1.5 L7 6.5 L13 1.5" stroke="#0aa1dc" stroke-width="1.4" fill="none"/>
          </svg>
          <span>014-555-0192</span>
        </div>
        <div class="contact-row">
          <svg width="14" height="14" viewBox="0 0 14 14" aria-hidden="true">
            <circle cx="7" cy="7" r="6" fill="none" stroke="#333" stroke-width="1.4"/>
            <ellipse cx="7" cy="7" rx="2.6" ry="6" fill="none" stroke="#333" stroke-width="1.2"/>
            <line x1="1" y1="7" x2="13" y2="7" stroke="#333" stroke-width="1.2"/>
          </svg>
          <span>www.hearthwise.net</span>
        </div>
        <div class="contact-address">Portland, Oregon, 97201 United States of America</div>
        <div class="social">
          <span class="social-item social-a" role="img" aria-label="Social network link"></span>
          <span class="social-item social-b" role="img" aria-label="Social network link"></span>
          <span class="social-item social-c" role="img" aria-label="Social network link"></span>
        </div>
      </div>
    </section>
    <div class="copyright">© 2015 Hearthwise Smart Home Automation all right reserved</div>
  </footer>
</body>
</html>
```